van Kalder Jewelry & Co. needs a website design

We need a website design for a new company based in Minnesota called 'van Kalder Jewelry & Co.' My wife and I are both geologists who handcraft fine jewelry using nephrite-jade from a newly discovered glacial deposit in Minnesota that I independently discovered, researched, and extracted. The jade colors range from a beautiful black to dark green and are mostly set in yellow gold, though we also use silver, platinum, and white gold. We will also be using nephrite-jade, jadeite-jade's from other parts of the world, including other semi- precious and precious stones such as black onyx/ chalcedony's, rubies ,sapphire, and diamonds. The family name 'van Kalder' means of the ash tree in French, and I would this motif to be incorporated into the website design. I've attached the files for our company logo and would like to blend that theme and emblem into the design as well in an elegant fashion. I'm aiming for a black jade/ dark green and yellow gold look am primarily interested in a design optimized for online shoppers. Additionally, I want a section where visitors can read a brief summary of our research and discovery story as geologists. Currently, we will be selling pendant necklaces, bead necklaces, earrings, bead bracelets, and bracelets. The website should convey that we sell fine, handcrafted, and very unique jewelry.

```html
<!DOCTYPE html>
<html lang="en">
<head>
<meta charset="utf-8">
<title>van Kalder Jewelry &amp; Co.</title>
<link rel="stylesheet" href="https://fonts.googleapis.com/css2?family=Cinzel:wght@400;500;600&family=Roboto:wght@400;500;700&display=swap">
<style>
:root{
  --black:#000;
  --ink:#0b0b0b;
  --panel:#121212;
  --gold:#b8973a;
  --gold-light:#c9ad4f;
  --white:#fff;
  --line:#2b2b2b;
}
*{margin:0;padding:0;box-sizing:border-box}
html,body{width:1200px;height:3877px;overflow:hidden;background:var(--black)}
body{position:relative;font-family:'Roboto',Arial,sans-serif;color:var(--white)}
.heading{font-family:'Cinzel',Georgia,serif;font-weight:500;letter-spacing:1px;text-align:center;position:absolute;left:0;width:1200px;line-height:1}
.underline{position:absolute;left:553px;width:94px;height:3px;background:var(--gold)}

/* header */
.top-rule{position:absolute;left:0;top:0;width:1200px;height:4px;background:var(--gold)}
.header{position:absolute;left:0;top:4px;width:1200px;height:196px;background:var(--black)}
.search{position:absolute;left:111px;top:43px;width:309px;height:42px;border:1px solid #3a3a3a;display:flex;align-items:center;padding-left:18px;font-size:13px;color:#ddd}
.search svg{margin-right:8px}
.brand{position:absolute;left:450px;top:10px;width:300px;text-align:center;font-family:'Cinzel',Georgia,serif;font-weight:400;color:var(--white)}
.brand-mark{width:24px;height:24px;background:var(--gold);margin:6px auto 14px}
.brand-name{font-size:22px;letter-spacing:2px;line-height:1}
.brand-sub{font-size:8px;letter-spacing:3px;margin-top:6px;color:var(--gold)}
.account{position:absolute;top:50px;display:flex;align-items:center;font-size:13px;font-weight:500}
.gem{width:30px;height:30px;background:var(--gold);transform:rotate(45deg);display:flex;align-items:center;justify-content:center;margin-right:18px}
.gem svg{transform:rotate(-45deg)}
.nav-rule{position:absolute;left:111px;top:132px;width:978px;height:1px;background:var(--line)}
.nav{position:absolute;top:157px;left:0;width:1200px;display:flex;justify-content:center;gap:57px;font-size:14px;font-weight:500}
.nav a{color:var(--white);text-decoration:none}
.nav a.active{color:var(--gold);border-bottom:1px solid var(--gold);padding-bottom:4px}
.nav .caret{display:inline-block;margin-left:6px;border-left:5px solid transparent;border-right:5px solid transparent;border-top:5px solid #fff;vertical-align:middle}

/* hero */
.hero{position:absolute;left:0;top:200px;width:1200px;height:545px;
  background:
    radial-gradient(ellipse 420px 160px at 250px 440px,rgba(28,84,78,.55),rgba(28,84,78,0)),
    linear-gradient(180deg,rgba(0,0,0,0) 78%,rgba(20,26,24,.7) 100%),
    radial-gradient(ellipse at 35% 20%,#8fa098 0%,#5e6c67 38%,#333c39 75%,#222826 100%)}
.hero-title{position:absolute;left:600px;top:134px;font-family:'Cinzel',Georgia,serif;font-size:52px;line-height:57px;letter-spacing:1px;font-weight:600}
.hero-text{position:absolute;left:598px;top:268px;width:440px;font-size:20px;line-height:31px}
.btn-gold{position:absolute;background:var(--gold);color:var(--white);font-size:14px;font-weight:500;display:flex;align-items:center;justify-content:center}
.hero-dots{position:absolute;left:1135px;top:228px;display:flex;flex-direction:column;gap:16px}
.hdot{width:10px;height:10px;border:1.5px solid #fff;transform:rotate(45deg)}
.hdot.on{background:var(--gold);border-color:var(--gold)}

/* categories */
.categories{position:absolute;left:0;top:745px;width:1200px;height:916px;background:var(--ink)}
.tile{position:absolute;overflow:hidden}
.tile-label{position:absolute;left:32px;bottom:35px;font-size:17px;font-weight:500;color:#151515}
.tile.active{border:4px solid var(--gold)}
.tile.active .tile-label{left:28px;bottom:31px}
.arrow-gem{position:absolute;right:32px;bottom:34px;width:26px;height:26px;background:var(--gold);transform:rotate(45deg);display:flex;align-items:center;justify-content:center}
.arrow-gem svg{transform:rotate(-45deg)}

/* products */
.featured{position:absolute;left:0;top:1661px;width:1200px;height:640px;background:linear-gradient(180deg,#1b1b1b 0%,#2a2a2a 40%,#1d1d1d 75%,#141414 100%)}
.bestsellers{position:absolute;left:0;top:2858px;width:1200px;height:698px;background:var(--ink)}
.card{position:absolute;width:243px;height:332px;background:var(--panel)}
.card.active{border:3px solid var(--gold)}
.card-img{position:absolute;left:9px;top:9px;width:217px;height:222px;background:#fff}
.card.active .card-img{left:6px;top:6px}
.img-turq{background:radial-gradient(ellipse 70px 90px at 50% 50%,#bfe8ea 0%,#e8f7f7 55%,#fff 100%)}
.img-jade{background:radial-gradient(ellipse 100px 70px at 50% 55%,#c9d3cf 0%,#eef1f0 60%,#fff 100%)}
.img-bead{background:radial-gradient(ellipse 100px 50px at 50% 50%,#c3ecef 0%,#eaf8f9 60%,#fff 100%)}
.img-silver{background:radial-gradient(ellipse 90px 80px at 50% 50%,#d6d6d6 0%,#f1f1f1 60%,#fff 100%)}
.card-title{position:absolute;left:12px;top:250px;font-size:13px;font-weight:700}
.card-price{position:absolute;right:12px;top:250px;font-size:13px;font-weight:700}
.card-rule{position:absolute;left:12px;right:12px;top:276px;height:1px;background:var(--line)}
.card-link{position:absolute;left:12px;top:295px;font-size:10px;font-weight:700;color:var(--gold);text-decoration:underline}
.cart-gem{position:absolute;right:16px;top:290px;width:20px;height:20px;background:var(--gold);transform:rotate(45deg);display:flex;align-items:center;justify-content:center}
.cart-gem svg{transform:rotate(-45deg)}
.card.active .card-title,.card.active .card-price{top:247px}
.dots{position:absolute;left:0;width:1200px;display:flex;justify-content:center;gap:14px}
.dot{width:8px;height:8px;background:#fff;transform:rotate(45deg)}
.dot.on{background:var(--gold)}

/* story */
.story{position:absolute;left:0;top:2301px;width:1200px;height:557px}
.story-photo{position:absolute;left:0;top:0;width:600px;height:557px;background:radial-gradient(ellipse at 55% 45%,#b9b9b9 0%,#8a8a8a 40%,#4f4f4f 80%,#333 100%)}
.story-panel{position:absolute;left:600px;top:0;width:600px;height:557px;background:linear-gradient(135deg,#b99a3b 0%,#c6a948 55%,#c9b04e 100%)}
.story-title{position:absolute;left:59px;top:90px;font-family:'Cinzel',Georgia,serif;font-weight:500;font-size:44px;letter-spacing:1px;line-height:1.1}
.story-text{position:absolute;left:59px;width:432px;font-size:14px;line-height:25.5px;text-align:justify}
.btn-white{position:absolute;left:59px;top:409px;width:141px;height:49px;background:#fff;color:#1a1a1a;font-size:14px;font-weight:500;display:flex;align-items:center;justify-content:center}

/* footer */
.footer{position:absolute;left:0;top:3556px;width:1200px;height:321px;background:var(--ink)}
.foot-head{position:absolute;top:64px;font-size:20px;font-weight:700}
.foot-link{position:absolute;font-size:15px}
.email-line{position:absolute;left:595px;top:158px;width:299px;height:1px;background:#777}
.contact{position:absolute;left:595px;top:194px;display:flex;align-items:center;gap:10px;font-size:12px}
.social{width:10px;height:10px;border-radius:50%;background:#fff}
.foot-rule{position:absolute;left:111px;top:262px;width:978px;height:1px;background:var(--line)}
.pay{position:absolute;top:275px;display:flex;gap:4px;left:839px}
.pay span{width:47px;height:26px;border-radius:3px;background:#d9d9d9}
</style>
</head>
<body>

<div class="top-rule"></div>
<header class="header">
  <div class="search">
    <svg width="13" height="13" viewBox="0 0 14 14"><circle cx="6" cy="6" r="4.5" fill="none" stroke="#b8973a" stroke-width="2"/><line x1="9.5" y1="9.5" x2="13" y2="13" stroke="#b8973a" stroke-width="2"/></svg>
    Search . . .
  </div>
  <div class="brand">
    <div class="brand-mark"></div>
    <div class="brand-name">VAN KALDER</div>
    <div class="brand-sub">JEWELRY &amp; CO.</div>
  </div>
  <div class="account" style="left:862px">
    <div class="gem"><svg width="12" height="12" viewBox="0 0 12 12"><circle cx="6" cy="3.5" r="2.6" fill="#fff"/><path d="M1 12c0-3 2.2-5 5-5s5 2 5 5z" fill="#fff"/></svg></div>
    LOGIN
  </div>
  <div class="account" style="left:998px">
    <div class="gem"><svg width="12" height="12" viewBox="0 0 12 12"><path d="M4 4V3a2 2 0 0 1 4 0v1" fill="none" stroke="#fff" stroke-width="1.3"/><rect x="1.5" y="4" width="9" height="7.5" fill="#fff"/></svg></div>
    $0.00
  </div>
  <div class="nav-rule"></div>
  <nav class="nav">
    <a class="active">HOME</a>
    <a>ABOUT US</a>
    <a>FEATURED PRODUCTS<span class="caret"></span></a>
    <a>BLOG</a>
    <a>CONTACT US</a>
  </nav>
</header>

<section class="hero">
  <div role="img" aria-label="Misty green stone backdrop with a ring of dark jade beads on a ledge" style="position:absolute;inset:0"></div>
  <h1 class="hero-title">VAN KALDER<br>JEWELRY &amp; CO.</h1>
  <p class="hero-text">Lorem ipsum dolor sit amet consectetur adipis elit sed do eiusmod temporea.</p>
  <div class="btn-gold" style="left:599px;top:351px;width:124px;height:50px">SHOP NOW</div>
  <div class="hero-dots">
    <div class="hdot"></div><div class="hdot on"></div><div class="hdot"></div><div class="hdot"></div>
  </div>
</section>

<section class="categories">
  <h2 class="heading" style="top:144px;font-size:46px">PRODUCT CATEGORIES</h2>
  <div class="underline" style="top:201px"></div>

  <div class="tile" style="left:111px;top:256px;width:481px;height:282px;background:radial-gradient(ellipse at 30% 25%,#ececec 0%,#bdbdbd 45%,#8c8c8c 100%)" role="img" aria-label="Jeweler arranging stones for pendant necklaces">
    <span class="tile-label">PENDANT NECKLACES</span>
    <div class="arrow-gem"><svg width="12" height="12" viewBox="0 0 12 12"><path d="M2 2l4 4-4 4M6 2l4 4-4 4" fill="none" stroke="#fff" stroke-width="1.6"/></svg></div>
  </div>
  <div class="tile" style="left:608px;top:256px;width:481px;height:282px;background:radial-gradient(ellipse at 40% 60%,#e3e3e3 0%,#c8c8c8 50%,#9e9e9e 100%)" role="img" aria-label="Bead necklaces laid on sand">
    <span class="tile-label">BEAD NECKLACES</span>
    <div class="arrow-gem"><svg width="12" height="12" viewBox="0 0 12 12"><path d="M2 2l4 4-4 4M6 2l4 4-4 4" fill="none" stroke="#fff" stroke-width="1.6"/></svg></div>
  </div>
  <div class="tile" style="left:111px;top:554px;width:315px;height:231px;background:radial-gradient(ellipse at 50% 45%,#a7a7a7 0%,#cdcdcd 55%,#e0e0e0 100%)" role="img" aria-label="Ornate silver earrings among leaves">
    <span class="tile-label">EARRINGS</span>
    <div class="arrow-gem"><svg width="12" height="12" viewBox="0 0 12 12"><path d="M2 2l4 4-4 4M6 2l4 4-4 4" fill="none" stroke="#fff" stroke-width="1.6"/></svg></div>
  </div>
  <div class="tile active" style="left:444px;top:554px;width:312px;height:231px;background:radial-gradient(ellipse 110px 120px at 78% 40%,#cdeff0 0%,#eef9f9 55%,#fff 100%)" role="img" aria-label="Hand wearing turquoise bead bracelets">
    <span class="tile-label">BEAD BRACELETS</span>
    <div class="arrow-gem" style="right:28px;bottom:30px"><svg width="12" height="12" viewBox="0 0 12 12"><path d="M2 2l4 4-4 4M6 2l4 4-4 4" fill="none" stroke="#fff" stroke-width="1.6"/></svg></div>
  </div>
  <div class="tile" style="left:772px;top:554px;width:317px;height:231px;background:linear-gradient(120deg,#8f8f8f 0%,#c9c9c9 45%,#e6e6e6 70%,#a0a0a0 100%)" role="img" aria-label="Wrist wearing fine bracelets">
    <span class="tile-label">BRACELETS</span>
    <div class="arrow-gem"><svg width="12" height="12" viewBox="0 0 12 12"><path d="M2 2l4 4-4 4M6 2l4 4-4 4" fill="none" stroke="#fff" stroke-width="1.6"/></svg></div>
  </div>
</section>

<section class="featured" aria-label="Featured products over a dusky landscape">
  <h2 class="heading" style="top:74px;font-size:46px">FEATURED PRODUCTS</h2>
  <div class="underline" style="top:129px"></div>

  <div class="card" style="left:102px;top:183px">
    <div class="card-img img-turq" role="img" aria-label="Turquoise drop earrings"></div>
    <span class="card-title">PRODUCT TITLE</span><span class="card-price">$50.00</span>
    <div class="card-rule"></div><span class="card-link">SHOP NOW</span>
    <div class="cart-gem"><svg width="10" height="10" viewBox="0 0 10 10"><path d="M1 2h2l1 4h5l1-3H3.5" fill="#fff"/><circle cx="4.5" cy="8.5" r="1" fill="#fff"/><circle cx="8" cy="8.5" r="1" fill="#fff"/></svg></div>
  </div>
  <div class="card" style="left:355px;top:183px">
    <div class="card-img img-jade" role="img" aria-label="Green jade bead bracelet beside a ring box"></div>
    <span class="card-title">PRODUCT TITLE</span><span class="card-price">$50.00</span>
    <div class="card-rule"></div><span class="card-link">SHOP NOW</span>
    <div class="cart-gem"><svg width="10" height="10" viewBox="0 0 10 10"><path d="M1 2h2l1 4h5l1-3H3.5" fill="#fff"/><circle cx="4.5" cy="8.5" r="1" fill="#fff"/><circle cx="8" cy="8.5" r="1" fill="#fff"/></svg></div>
  </div>
  <div class="card active" style="left:607px;top:181px;width:240px;height:335px">
    <div class="card-img img-bead" role="img" aria-label="Turquoise bead bracelet"></div>
    <span class="card-title">PRODUCT TITLE</span><span class="card-price">$50.00</span>
    <div class="card-rule" style="top:273px"></div><span class="card-link" style="top:292px">SHOP NOW</span>
    <div class="cart-gem" style="top:287px"><svg width="10" height="10" viewBox="0 0 10 10"><path d="M1 2h2l1 4h5l1-3H3.5" fill="#fff"/><circle cx="4.5" cy="8.5" r="1" fill="#fff"/><circle cx="8" cy="8.5" r="1" fill="#fff"/></svg></div>
  </div>
  <div class="card" style="left:862px;top:183px">
    <div class="card-img img-silver" role="img" aria-label="Silver drop earrings and pendant"></div>
    <span class="card-title">PRODUCT TITLE</span><span class="card-price">$50.00</span>
    <div class="card-rule"></div><span class="card-link">SHOP NOW</span>
    <div class="cart-gem"><svg width="10" height="10" viewBox="0 0 10 10"><path d="M1 2h2l1 4h5l1-3H3.5" fill="#fff"/><circle cx="4.5" cy="8.5" r="1" fill="#fff"/><circle cx="8" cy="8.5" r="1" fill="#fff"/></svg></div>
  </div>
  <div class="dots" style="top:556px"><div class="dot"></div><div class="dot on"></div><div class="dot"></div><div class="dot"></div></div>
</section>

<section class="story">
  <div class="story-photo" role="img" aria-label="Black and white portrait of the founding couple"></div>
  <div class="story-panel">
    <h2 class="story-title">OUR STORY</h2>
    <p class="story-text" style="top:158px">Lorem ipsum dolor sit amet, consectetur adipiscing elit, sed do eiusmod tempor incididunt ut labore et dolore magna aliqua. Ut enim ad minim veniam, quis nostrud exercitation ullamco laboris nisi ut aliquip ex ea commodo consequat. Duis aute irure dolor in in dolore eu fugiat nullea.</p>
    <p class="story-text" style="top:298px">Lorem ipsum dolor sit amet, consectetur adipiscing elit, sed do eiusmod tempor incididunt ut labore et dolore magna aliqua. Ut enim ad minim veniam, quis nostrudea.</p>
    <div class="btn-white">LEARN MORE</div>
  </div>
</section>

<section class="bestsellers">
  <h2 class="heading" style="top:126px;font-size:46px">BEST SELLERS</h2>
  <div class="underline" style="top:181px"></div>

  <div class="card" style="left:102px;top:229px">
    <div class="card-img img-turq" role="img" aria-label="Turquoise drop earrings"></div>
    <span class="card-title">PRODUCT TITLE</span><span class="card-price">$50.00</span>
    <div class="card-rule"></div><span class="card-link">SHOP NOW</span>
    <div class="cart-gem"><svg width="10" height="10" viewBox="0 0 10 10"><path d="M1 2h2l1 4h5l1-3H3.5" fill="#fff"/><circle cx="4.5" cy="8.5" r="1" fill="#fff"/><circle cx="8" cy="8.5" r="1" fill="#fff"/></svg></div>
  </div>
  <div class="card" style="left:355px;top:229px">
    <div class="card-img img-jade" role="img" aria-label="Green jade bead bracelet beside a ring box"></div>
    <span class="card-title">PRODUCT TITLE</span><span class="card-price">$50.00</span>
    <div class="card-rule"></div><span class="card-link">SHOP NOW</span>
    <div class="cart-gem"><svg width="10" height="10" viewBox="0 0 10 10"><path d="M1 2h2l1 4h5l1-3H3.5" fill="#fff"/><circle cx="4.5" cy="8.5" r="1" fill="#fff"/><circle cx="8" cy="8.5" r="1" fill="#fff"/></svg></div>
  </div>
  <div class="card active" style="left:607px;top:227px;width:240px;height:335px">
    <div class="card-img img-bead" role="img" aria-label="Turquoise bead bracelet"></div>
    <span class="card-title">PRODUCT TITLE</span><span class="card-price">$50.00</span>
    <div class="card-rule" style="top:273px"></div><span class="card-link" style="top:292px">SHOP NOW</span>
    <div class="cart-gem" style="top:287px"><svg width="10" height="10" viewBox="0 0 10 10"><path d="M1 2h2l1 4h5l1-3H3.5" fill="#fff"/><circle cx="4.5" cy="8.5" r="1" fill="#fff"/><circle cx="8" cy="8.5" r="1" fill="#fff"/></svg></div>
  </div>
  <div class="card" style="left:862px;top:229px">
    <div class="card-img img-silver" role="img" aria-label="Silver drop earrings and pendant"></div>
    <span class="card-title">PRODUCT TITLE</span><span class="card-price">$50.00</span>
    <div class="card-rule"></div><span class="card-link">SHOP NOW</span>
    <div class="cart-gem"><svg width="10" height="10" viewBox="0 0 10 10"><path d="M1 2h2l1 4h5l1-3H3.5" fill="#fff"/><circle cx="4.5" cy="8.5" r="1" fill="#fff"/><circle cx="8" cy="8.5" r="1" fill="#fff"/></svg></div>
  </div>
  <div class="dots" style="top:601px"><div class="dot"></div><div class="dot on"></div><div class="dot"></div><div class="dot"></div></div>
</section>

<footer class="footer">
  <h3 class="foot-head" style="left:111px">QUICK LINKS</h3>
  <span class="foot-link" style="left:111px;top:121px">Home</span>
  <span class="foot-link" style="left:111px;top:156px">About Us</span>
  <span class="foot-link" style="left:111px;top:190px">Featured Products</span>
  <span class="foot-link" style="left:111px;top:225px">Blog</span>
  <span class="foot-link" style="left:334px;top:121px">Privacy Policy</span>
  <span class="foot-link" style="left:334px;top:156px">Shipping &amp; Returns</span>
  <span class="foot-link" style="left:334px;top:190px">Contact Us</span>

  <h3 class="foot-head" style="left:595px">JOIN OUR NEWSLETTER</h3>
  <span class="foot-link" style="left:595px;top:125px;font-size:13px">Enter Your Email Here</span>
  <div class="email-line"></div>
  <div class="btn-gold" style="left:932px;top:113px;width:136px;height:49px;font-size:15px">SUBSCRIBE</div>
  <div class="contact">
    <svg width="11" height="11" viewBox="0 0 12 12"><path d="M2.5 1l2 2.5-1.2 1.3a7 7 0 0 0 3.9 3.9L8.5 7.5 11 9.5 9.7 11C5 10.5 1.5 7 1 2.3z" fill="#b8973a"/></svg>
    <span>+1 (612) 555 0142</span><span style="margin:0 8px">|</span>
    <svg width="12" height="9" viewBox="0 0 12 9"><rect width="12" height="9" fill="#b8973a"/><path d="M0 0l6 5 6-5" fill="none" stroke="#0b0b0b" stroke-width="1"/></svg>
    <span>info@vankalder.example</span><span style="margin:0 8px">|</span>
    <span class="social"></span><span class="social"></span><span class="social"></span>
  </div>

  <div class="foot-rule"></div>
  <span class="foot-link" style="left:111px;top:282px;font-size:12px">© 2024 van Kalder Jewelry &amp; Co. &nbsp;|&nbsp; All Rights Reserved</span>
  <div class="pay"><span></span><span></span><span></span><span></span><span></span></div>
</footer>

</body>
</html>
```